Gestaltung eines Merkblattes
Ein Entwurf, der genau meinen Vorstellungen entspricht. Eine Abwicklung, die schneller und professioneller nicht sein könnte. Die Kommunikation - sehr symphatisch und kundenorientiert. Resumee: Besser geht es nicht.
Zielgruppe
www.tierklang-analytik.de/ Medizinische Bioresonanzanalysen für Pferde. Die Kundschaft besteht hauptsächlich aus Frauen, Alter von 20- 55 Jahre.
Bei dem Projekt handelt es sich um die Gestaltung eines wichtigen Merkblattes, das jedem Kunde zusammen mit dem Befund der Analyse gemailt wird. Es enthält wichtige Informationen rund um die Bioresonanzanalyse und sollte als pdf- Datei vorliegen.
Aufgabenstellung
Kernproblem: Die Kunden lesen das Merkblatt gar nicht oder nicht sorgfältig. So entstehen viele Fragen in der Folge, die nicht notwendig wären.
Wir benötigen eine pdf- Datei, die zum Lesen anregt, gerne gelesen wird und in der die wichtigsten Aspekte in das Auge fallen. Diese wurden von mir in der Worddatei, die den Text enthält, rot markiert.
Der Text in schwarz ist deutlich weniger wichtig.
Ach ja, die Überschrift ist doof. 'Allgemeine Hinweise' das animiert nicht wirklich zum Lesen. Falls Sie eine griffige Idee haben, sehr gerne.

```html
<!DOCTYPE html>
<html lang="de">
<head>
<meta charset="utf-8">
<title>Merkblatt – Medizinische Bioresonanzanalysen für Pferde</title>
<link href="https://fonts.googleapis.com/css2?family=Ubuntu:wght@300;400;500;700&display=swap" rel="stylesheet">
<style>
:root{
  --olive:#a4ad5c;
  --olive-dark:#8c954a;
  --olive-panel:rgba(164,173,92,.88);
  --paper:rgba(240,241,236,.93);
  --sky:#b9c4cf;
  --ink:#6a6d70;
  --white:#ffffff;
  --bg:#ffffff;
}
*{box-sizing:border-box;margin:0;padding:0}
html,body{width:1042px;height:1200px;overflow:hidden;background:var(--bg)}
body{font-family:'Ubuntu',sans-serif;color:var(--ink);position:relative}
.page{position:absolute;top:268px;width:470px;height:665px;overflow:hidden;box-shadow:0 4px 14px rgba(0,0,0,.28)}
.page--front{left:34px;background:linear-gradient(180deg,#a3aab3 0%,#b2b8bf 45%,#a9b0b8 100%)}
.page--back{left:538px;background:#c9ced4}
.abs{position:absolute}
.photo-mountains{left:0;top:0;width:470px;height:340px;background:linear-gradient(180deg,#c9ced2 0%,#8d939a 40%,#6f757c 70%,#a3aab3 100%)}
.photo-horse{left:0;top:200px;width:470px;height:465px;background:linear-gradient(180deg,#aeb9c4 0%,#7d8890 35%,#5b5650 60%,#8a8272 85%,#a79e8d 100%)}
.doc-title{right:22px;top:18px;text-align:right;font-weight:300;font-size:20px;line-height:1.12;color:#f4f5f2}
.band{background:var(--olive);color:var(--white);font-weight:700;text-transform:uppercase;letter-spacing:.5px}
.band--gilt{left:256px;top:100px;width:214px;height:24px;font-size:15px;padding:3px 10px}
.card{background:var(--paper);font-size:7.4px;line-height:1.45;padding:10px 10px;overflow:hidden}
.card b{color:var(--olive-dark);font-weight:700}
.card .big{font-size:10.5px}
.num{width:24px;height:24px;border-radius:50%;background:var(--olive);color:var(--white);font-weight:700;font-size:12px;display:flex;align-items:center;justify-content:center;border:2px solid #f4f5f0}
.num--alert{background:var(--white);color:var(--olive-dark);border:2px solid var(--olive)}
.heading{color:var(--white);font-weight:700;font-size:15px;text-transform:uppercase;letter-spacing:.4px}
.ticks{list-style:none;font-size:7.4px;color:#f2f3ee}
.ticks li{border-bottom:1px solid var(--olive);padding:3px 0 3px 12px;position:relative}
.ticks li::before{content:"";position:absolute;left:0;top:5px;width:6px;height:6px;background:#f2f3ee}
.side-tab{left:24px;top:455px;width:30px;height:198px;background:var(--olive)}
.side-tab span{position:absolute;left:50%;top:50%;transform:translate(-50%,-50%) rotate(-90deg);color:var(--white);font-weight:700;font-size:14px;letter-spacing:.6px;white-space:nowrap}
.panel{background:var(--olive-panel);color:var(--white);font-size:7.2px;line-height:1.5;padding:8px 12px;overflow:hidden}
.panel ul{list-style:none}
.panel li::before{content:"– "}
.head-right{right:14px;text-align:right}
.band--tierarzt{left:0;top:18px;width:126px;height:32px;font-size:15px;padding:7px 22px}
.strip{left:126px;top:18px;width:300px;height:32px;background:var(--paper);font-size:6.8px;line-height:1.4;padding:4px 8px}
.band--doping{left:232px;top:310px;width:238px;height:20px;background:var(--sky);text-align:right;color:var(--white);font-weight:700;font-size:14px;padding:2px 14px}
.brand-title{left:20px;top:480px;color:var(--white);font-weight:700;font-size:13px;line-height:1.15}
.brand-mark{left:20px;top:540px;width:78px;height:70px;background:var(--white);display:flex;flex-direction:column;align-items:center;justify-content:center;gap:5px}
.brand-mark i{width:16px;height:16px;background:var(--olive);display:block}
.brand-mark span{font-size:8.5px;font-weight:500;color:var(--olive-dark);text-align:center;line-height:1.1}
.contact{left:106px;top:548px;width:115px;font-size:6.6px;line-height:1.45;color:var(--white)}
</style>
</head>
<body>

<section class="page page--front">
  <div class="abs photo-mountains" role="img" aria-label="Nebelige Berglandschaft mit dunklen Gipfeln"></div>
  <h1 class="abs doc-title">Medizinische<br>Bioresonanzanalysen<br>für Pferde</h1>
  <div class="abs band band--gilt">Grundsätzlich gilt…</div>

  <div class="abs card" style="left:24px;top:140px;width:182px;height:200px;padding-top:18px">
    <p>Die <b class="big">empfohlenen Präparate</b> können (wenn nicht anders angegeben) in das normale Kraftfutter gegeben werden. Tropfen und Bachblüten bitte auf ein kleines Stück trockenes Brot, Zwieback, bei Pferden, die kein Getreide fressen dürfen, auf ein Stück Reiswaffel geben, und dem Pferd direkt füttern.</p>
    <p style="margin-top:8px"><b class="big" style="font-style:italic">Kräuterbasis Pulver</b> muss nicht, wie vom Hersteller angegeben, in Wasser aufgelöst werden. Eine Gabe in das Kraftfutter, feucht oder trocken, verändert nicht die Wirkung.</p>
  </div>
  <div class="abs num" style="left:103px;top:127px">1</div>

  <div class="abs card" style="left:240px;top:132px;width:206px;height:110px;padding-left:16px">
    <p>Falls Ihr Pferd sehr <b class="big">wählerisch</b> ist <b class="big">bei der Zufütterung</b> von Präparaten in Pellets- oder Pulverform, dann beginnen Sie mit einer sehr kleinen Dosierung und steigern diese sehr langsam. Bei trockenem Futter (Müsli, Hafer) sortieren manche Pferde gerne aus. Hier ist es sinnvoll, das Futter anzufeuchten oder etwas Heucobs dazuzugeben.</p>
  </div>
  <div class="abs num" style="left:228px;top:175px">2</div>

  <div class="abs card" style="left:240px;top:250px;width:206px;height:88px;padding-left:16px">
    <p>Bitte <b class="big">füttern</b> Sie alle Präparate, außer es sind abweichende Empfehlungen vorhanden, <b class="big">ohne Unterbrechung</b>, bis Ihnen das Ergebnis der erneuten Nachtestung vorliegt. Längere Pausen können die positive Entwicklung Ihres Pferdes beeinträchtigen.</p>
  </div>
  <div class="abs num" style="left:228px;top:280px">3</div>

  <h2 class="abs heading" style="left:24px;top:348px">Nachtestung</h2>
  <ul class="abs ticks" style="left:24px;top:370px;width:270px">
    <li>Wir bestätigen den Eingang der Probe zur Nachtestung nicht.</li>
    <li>In regelmäßigen Abständen werden alle Befunde nachgetestet.</li>
    <li>Wir senden Ihnen im Anschluss per Mail das neue Ergebnis mit</li>
    <li>einer aktualisierten Therapieempfehlung zu.</li>
  </ul>
  <div class="abs card" style="left:318px;top:352px;width:128px;height:92px;padding-left:22px">
    <p>Wir brauchen für die Nachtestung eine neue Haarprobe und ein kurzes Feedback zu der aktuellen Entwicklung Ihres Pferdes. Mehr nicht.</p>
  </div>
  <div class="abs num num--alert" style="left:304px;top:354px">!</div>

  <div class="abs side-tab"><span>BACHBLÜTEN</span></div>
  <div class="abs card" style="left:54px;top:455px;width:392px;height:82px;padding:10px 14px">
    <p>Wenn die Therapieempfehlung eine Übersicht an Bachblüten enthält, dann spiegeln diese den <b class="big">seelischen Zustand</b> Ihres Pferdes wieder, der von seinen bisherigen Lebensbedingungen, seiner körperlichen Belastung durch Krankheit und durch Abläufe in seiner Herde beeinflusst wird. Erfahrungsgemäß bezieht sich die Darstellung der Blüten bei Pferden, die in einer Herde leben, häufig mehr auf die Gefühle des Pferdes gegenüber seinen Artgenossen als auf den Kontakt mit dem Menschen.</p>
  </div>
  <div class="abs panel" style="left:54px;top:537px;width:392px;height:116px;background:transparent">
    <p style="font-weight:700;border-bottom:1px solid var(--olive);padding-bottom:3px">Die meisten Apotheken verkaufen Bachblüten in kleinen Mengen zur Mischung.</p>
    <ul style="margin-top:5px;color:#f2f3ee">
      <li>Bitte setzen Sie die Bachblüten laut Therapieempfehlung selbst an.</li>
      <li>10 ml Wasser mit etwas Obstessig verwenden.</li>
      <li>Jeweils zwei Tropfen jeder Blüte zugeben und gut schütteln.</li>
      <li>Drei Tropfen am Tag direkt füttern, bis die Flasche leer ist.</li>
      <li>Bei Rückfragen zur Mischung wenden Sie sich an uns.</li>
    </ul>
  </div>
</section>

<section class="page page--back">
  <div class="abs photo-horse" role="img" aria-label="Braunes Pferd mit langer Mähne am Seeufer vor Berglandschaft"></div>

  <div class="abs band band--tierarzt">Tierarzt</div>
  <div class="abs strip">Wir weisen ausdrücklich darauf hin, dass die Ergebnisse der Bioresonanzanalyse nicht kompatibel sind mit den herkömmlichen Labormethoden und anderen tierärztlichen Diagnoseformen.</div>
  <div class="abs num num--alert" style="left:434px;top:22px">!</div>

  <div class="abs card" style="left:18px;top:62px;width:136px;height:146px">
    <p><b class="big">Beispiel</b>: Wenn wir eine Belastung der Leber mit dem Leberegel Fasciola hepatica feststellen, kann eine klassische Laboruntersuchung zu dem gleichen Thema ergebnislos bleiben. Der Grund liegt u. a. in der sehr unterschiedlichen Messempfindlichkeit.</p>
  </div>
  <div class="abs card" style="left:170px;top:62px;width:282px;height:64px;padding-left:18px">
    <p>Das Wohl Ihres Pferdes steht jederzeit im Mittelpunkt. Falls in der Zeit der Umsetzung der Therapieempfehlung bei Ihrem Pferd <b>Symptome auftreten</b>, die eine schnelle <b>Hilfe dringend erforderlich machen</b>, zögern Sie bitte nie, den <b>Tierarzt zu rufen</b>.</p>
  </div>
  <div class="abs num" style="left:158px;top:82px">1</div>
  <div class="abs card" style="left:170px;top:132px;width:282px;height:76px;padding-left:18px">
    <p>Bitte informieren Sie mich sofort, wenn Ihr Pferd zum Zeitpunkt der Nachtestung Medikamente vom Tierarzt erhält, etwa Antibiotika oder Cortison. Wir sprechen dann ab, ob die Nachtestung verschoben wird. Wurmkuren und Impfungen sind für die Nachtestung nicht von Bedeutung.</p>
  </div>
  <div class="abs num" style="left:158px;top:158px">2</div>

  <h2 class="abs heading head-right" style="top:216px">Impfung</h2>
  <div class="abs panel" style="left:232px;top:236px;width:238px;height:66px">
    <p>Wir geben generell keine Impfempfehlungen. Es hat sich jedoch in den vergangenen Jahren gezeigt, dass es sinnvoll ist, Impfungen zwischen den Phasen der Umsetzung der Therapieempfehlung anzusetzen. Werden sie zu einem späteren Zeitpunkt vorgenommen, kann es zu Rückschritten kommen.</p>
  </div>

  <div class="abs band--doping">DOPING</div>
  <div class="abs panel" style="left:232px;top:332px;width:238px;height:156px">
    <p>Zum Schutz der Pferde bestehen klare Doping-Richtlinien, die klare Regeln vorgeben, welche Zusatzfuttermittel oder Medikamente und auch Naturheilmittel vor Turnieren erlaubt sind. Dazu zählt auch die Einhaltung von Karenzzeiten vor einer Prüfung.</p>
    <p style="margin-top:5px">Bitte beachten Sie die Doping-Richtlinien der Pferdesportverbände und informieren Sie sich, ob die Präparate in unserer Therapieempfehlung eine Karenzzeit vor Prüfungsbeginn haben. Wenn Sie an einem Wettbewerb teilnehmen, empfehlen wir die Zufütterung vorher zu pausieren.</p>
    <p style="margin-top:5px">Wir übernehmen für Fragen einer Rückstellung der Präparate oder Meldepflichten keine Haftung.</p>
  </div>

  <h2 class="abs heading head-right" style="top:494px;line-height:1.05">Tragende Stuten<br>Stuten mit Fohlen bei Fuss</h2>
  <div class="abs panel" style="left:232px;top:530px;width:238px;height:78px">
    <p>Wir übernehmen keine Haftung für die Gabe der von uns empfohlenen Naturheilmittel bei tragenden Stuten und Stuten mit Fohlen bei Fuß. Die meisten Präparate sind unbedenklich, dennoch empfehlen wir, Rücksprache mit dem behandelnden Tierarzt zu halten.</p>
  </div>

  <p class="abs brand-title">Medizinische<br>Bioresonanzanalysen<br>für Pferde</p>
  <div class="abs brand-mark"><i></i><span>Tierklang<br>Analytik</span></div>
  <p class="abs contact">Therapeutin: Anna Weber<br>Hofweg 12, 79100 Musterstadt<br>Mail: info@tierklang-analytik.de<br>www.tierklang-analytik.de/<br>Stand: Oktober 2024</p>
</section>

</body>
</html>
```